Marketing firm Studio 847
Business card and stationery
Project: Marketing firm Studio 847
Marketing firm Studio 847  -
Creative Brief
Professional
Martin Kovalenko
Marketer, Business Strategist
Derveni, 14, 2385, Strovolia Nicosia Cyprus
Martin@studio-847.com
Www.studio-847.com
I need the logo and the dog on both, business cards and stationery. I need embossed logo or dog but I am also open to other designs.
He logo and the dog but I am also open to new design

```html
<!DOCTYPE html>
<html lang="en">
<head>
<meta charset="utf-8">
<title>Studio 847 — Business Card and Stationery</title>
<link href="https://fonts.googleapis.com/css2?family=Montserrat:wght@400;600;800&display=swap" rel="stylesheet">
<style>
  :root{
    --backdrop:#3b3b3d;
    --paper:#ffffff;
    --paper-shade:#e9e9ec;
    --brand:#9b59b6;
    --ink:#555559;
    --ink-light:#b5b5ba;
    --flap-dark:#1c1c1e;
  }
  *{box-sizing:border-box;margin:0;padding:0}
  html,body{width:1200px;height:310px;overflow:hidden;background:var(--backdrop)}
  body{font-family:"Montserrat",Arial,sans-serif;position:relative}
  .piece{position:absolute;background:var(--paper);box-shadow:0 2px 5px rgba(0,0,0,.45);overflow:hidden}
  .wordmark{font-weight:800;letter-spacing:.5px;color:var(--ink);white-space:nowrap;line-height:1}
  .wordmark .dot{display:inline-block;width:.35em;height:.35em;background:var(--brand);margin-left:.2em;vertical-align:top}
  .ghost{color:var(--paper-shade)}
  .tiny{font-size:4px;color:var(--ink);line-height:1.5;white-space:nowrap}

  .brand-block{position:absolute;left:24px;top:62px}
  .brand-block .wordmark{color:var(--paper);font-size:19px}
  .brand-block .tagline{color:var(--ink-light);font-size:5px;margin-top:5px;letter-spacing:1px;text-transform:uppercase}

  .card-front{left:24px;top:163px;width:108px;height:50px}
  .card-front .wordmark{position:absolute;left:8px;top:8px;font-size:9px}
  .card-front .band{position:absolute;left:0;right:0;bottom:0;height:20px;background:var(--brand)}
  .card-front .band .tiny{color:var(--paper);padding:4px 8px}
  .card-back-white{left:24px;top:232px;width:100px;height:48px}
  .card-back-white .wordmark{position:absolute;left:8px;top:10px;font-size:7px}
  .card-back-white .tiny{position:absolute;left:8px;bottom:6px}
  .card-back-purple{left:137px;top:232px;width:100px;height:48px;background:var(--brand)}
  .card-back-purple .wordmark{position:absolute;left:50%;top:50%;transform:translate(-50%,-50%);font-size:10px;color:var(--paper)}
  .card-back-purple .wordmark .dot{background:var(--paper)}

  .letterhead{top:19px;width:204px;height:269px}
  .letterhead-one{left:264px}
  .letterhead-two{left:492px}
  .letterhead .wordmark{position:absolute;left:16px;top:18px;font-size:13px}
  .letterhead .contact{position:absolute;right:16px;top:17px;text-align:right;color:var(--ink-light)}
  .letterhead .watermark{position:absolute;left:50%;top:48%;transform:translate(-50%,-50%);font-size:22px}
  .letterhead .footer{position:absolute;left:0;right:0;bottom:16px;text-align:center;color:var(--ink-light)}
  .letterhead-two .bottom-band{position:absolute;left:0;right:0;bottom:0;height:10px;background:var(--brand)}

  .slip{left:715px;width:221px;height:118px}
  .slip-one{top:24px}
  .slip-two{top:180px;height:106px}
  .slip .wordmark{position:absolute;left:12px;top:12px;font-size:11px}
  .slip .contact{position:absolute;right:12px;top:12px;text-align:right;color:var(--ink-light)}
  .slip .watermark{position:absolute;left:50%;top:52%;transform:translate(-50%,-50%);font-size:17px}
  .slip-two .bottom-band{position:absolute;left:0;right:0;bottom:0;height:12px;background:var(--brand)}

  .envelope{left:950px;width:226px;height:88px}
  .envelope svg{position:absolute;left:0;top:0;width:100%;height:100%}
  .envelope-dark{top:28px}
  .envelope-purple{top:108px}
  .envelope-white{top:212px;height:76px}
  .envelope .wordmark{position:absolute;left:50%;top:14px;transform:translateX(-50%);font-size:9px;color:var(--paper)}
  .envelope .wordmark .dot{background:var(--paper)}
</style>
</head>
<body>

<section class="brand-block">
  <div class="wordmark">STUDIO 847<span class="dot"></span></div>
  <p class="tagline">Marketing &amp; Business Strategy</p>
</section>

<article class="piece card-front">
  <div class="wordmark">STUDIO 847<span class="dot"></span></div>
  <div class="band">
    <p class="tiny"><strong>Account Director</strong><br>hello@studio-847.com</p>
  </div>
</article>

<article class="piece card-back-white">
  <div class="wordmark">STUDIO 847<span class="dot"></span></div>
  <p class="tiny">Main Street Office<br>Www.studio-847.com</p>
</article>

<article class="piece card-back-purple">
  <div class="wordmark">STUDIO 847<span class="dot"></span></div>
</article>

<article class="piece letterhead letterhead-one">
  <div class="wordmark">STUDIO 847<span class="dot"></span></div>
  <p class="tiny contact">Main Street Office<br>Suite 4, Floor 2<br>hello@studio-847.com</p>
  <div class="wordmark ghost watermark">STUDIO 847</div>
  <p class="tiny footer">Www.studio-847.com</p>
</article>

<article class="piece letterhead letterhead-two">
  <div class="wordmark">STUDIO 847<span class="dot"></span></div>
  <p class="tiny contact">Main Street Office<br>Suite 4, Floor 2<br>hello@studio-847.com</p>
  <div class="wordmark ghost watermark">STUDIO 847</div>
  <p class="tiny footer">Www.studio-847.com</p>
  <div class="bottom-band"></div>
</article>

<article class="piece slip slip-one">
  <div class="wordmark">STUDIO 847<span class="dot"></span></div>
  <p class="tiny contact">Main Street Office<br>hello@studio-847.com</p>
  <div class="wordmark ghost watermark">STUDIO 847</div>
</article>

<article class="piece slip slip-two">
  <div class="wordmark">STUDIO 847<span class="dot"></span></div>
  <p class="tiny contact">Main Street Office<br>hello@studio-847.com</p>
  <div class="wordmark ghost watermark">STUDIO 847</div>
  <div class="bottom-band"></div>
</article>

<article class="piece envelope envelope-dark">
  <svg viewBox="0 0 226 88" preserveAspectRatio="none" aria-hidden="true">
    <polygon points="0,0 226,0 113,46" fill="var(--flap-dark)"/>
    <polyline points="0,88 113,46 226,88" fill="none" stroke="var(--paper-shade)" stroke-width="1"/>
  </svg>
  <div class="wordmark">STUDIO 847<span class="dot"></span></div>
</article>

<article class="piece envelope envelope-purple">
  <svg viewBox="0 0 226 88" preserveAspectRatio="none" aria-hidden="true">
    <polygon points="0,0 226,0 113,50" fill="var(--brand)"/>
    <polyline points="0,88 113,50 226,88" fill="none" stroke="var(--paper-shade)" stroke-width="1"/>
  </svg>
  <div class="wordmark">STUDIO 847<span class="dot"></span></div>
</article>

<article class="piece envelope envelope-white">
  <svg viewBox="0 0 226 76" preserveAspectRatio="none" aria-hidden="true">
    <polyline points="0,0 113,38 226,0" fill="none" stroke="var(--paper-shade)" stroke-width="1.5"/>
    <polyline points="0,76 113,38 226,76" fill="none" stroke="var(--paper-shade)" stroke-width="1"/>
    <rect x="0" y="68" width="226" height="8" fill="var(--brand)"/>
  </svg>
</article>

</body>
</html>
```